Modern Web Design for Nonprofit Organization

Our client is looking to redesign their website. They want a modern look, clean and professional, that integrates their new brand guidelines.

Here is clients current site:
http://www.valorandes.org/

They want their own unique design but here are some sites the clients likes:
https://www.brixtonvane.com/en/
https://oakhollowrise.org/
https://www.lumacraft.com/
https://www.tbnlawgroup.com/
https://www.greyharborco.org/

Attached please find the clients logos, color palette, site plan and design specs.

You will create a homepage mockup that will have the following sections in this order:
1. Thin Alert Bar at very top with one line message
2. Nav Bar with Logo and Main Nav (red in site plan)
3. Hero Image or Video
4. Signup Bar with name email and zip and connect button
5. Intro section with image, welcome message, and supporter counter
6. Featured Action section with call to action
7. Event section with two upcoming event cards
8. Latest News section with three latest blog post
9. Support our work (donation) section
10. Worker and Member Stories Section with feed of social posts
11. Footer.

You can use text and images from clients existing site or placeholder images and placeholder text.

Please submit as many home page mockups/idea boards as you like. Client will pick the top three and ask for some revisions. If you are selected this will lead to a lot of work for this client.

Project is private please adhere to ArtPlenary terms of use and do not share any materials please.

QUICKEST RESPONSE PLEASE!

Thanks for looking!

Target Market(s)

Non profit donors and farmworker advocates

Number of Pages Required

2 page

Font styles to use
Sans Serif

Requirements
Must have
• Adhere to brief and client brand ID
Nice to have
• World class design

```html
<!DOCTYPE html>
<html lang="en">
<head>
<meta charset="utf-8">
<title>Valor Foundation — Home</title>
<link href="https://fonts.googleapis.com/css2?family=Jost:wght@300;400;500;600&family=Rubik:wght@400;700;800&display=swap" rel="stylesheet">
<style>
:root{
  --red:#dc0000;
  --dark:#25282d;
  --darker:#1d1f23;
  --grey:#ededed;
  --text:#4a4a4a;
  --ink:#1b1b1b;
  --white:#fff;
}
*{box-sizing:border-box;margin:0;padding:0}
html,body{width:1200px;height:4000px;overflow:hidden}
body{position:relative;background:var(--white);font-family:'Jost',sans-serif;color:var(--text)}
.abs{position:absolute}
.heading{font-family:'Rubik',sans-serif;font-weight:800;color:var(--ink);letter-spacing:.5px}
.rule{position:absolute;height:2px;width:50px;background:var(--red)}
.btn{position:absolute;display:flex;align-items:center;justify-content:center;border-radius:30px;font-family:'Rubik',sans-serif;font-weight:700;font-size:11px;letter-spacing:4px;text-transform:uppercase}
.btn-red{background:var(--red);color:var(--white)}
.btn-line{border:1.5px solid var(--white);color:var(--white)}
.photo{position:absolute}

/* alert */
.alert-bar{left:0;top:0;width:1200px;height:34px;background:var(--dark);color:#ddd;font-size:12px;display:flex;align-items:center;justify-content:center}
/* header */
.site-header{left:0;top:34px;width:1200px;height:109px;background:var(--white)}
.brand{left:93px;top:20px;display:flex;align-items:center;gap:8px;font-family:'Rubik',sans-serif;font-weight:700;font-size:16px;line-height:17px;color:var(--ink)}
.brand-dot{width:48px;height:48px;border-radius:50%;background:var(--red)}
.donate-top{left:992px;top:17px;width:112px;height:36px;border:1.5px solid var(--red);color:var(--red);font-size:10px}
.main-nav{left:481px;top:68px;width:719px;height:41px;background:var(--red);clip-path:polygon(30px 0,100% 0,100% 100%,0 100%);display:flex;align-items:center;justify-content:flex-end;gap:34px;padding-right:96px;color:var(--white);font-family:'Rubik',sans-serif;font-weight:700;font-size:13px}
/* hero */
.hero{left:0;top:143px;width:1200px;height:493px;background:linear-gradient(135deg,#7a5a46 0%,#a27a60 35%,#6b4c3b 70%,#4a3429 100%)}
.hero-title{left:93px;top:188px;font-family:'Rubik',sans-serif;font-weight:800;font-size:58px;line-height:56px;color:var(--white)}
.slides{right:93px;top:218px;text-align:right;font-family:'Rubik',sans-serif;font-weight:700;font-size:11px;color:var(--white);line-height:36px}
.slides .on{color:var(--red)}
/* grey band */
.intro-band{left:0;top:636px;width:1200px;height:564px;background:var(--grey)}
.signup{left:124px;top:599px;width:953px;height:152px;background:var(--dark)}
.signup h2{position:absolute;left:33px;top:18px;font-family:'Rubik',sans-serif;font-weight:800;font-size:33px;color:var(--white)}
.field{position:absolute;top:64px;height:40px;width:240px;background:var(--white);border-radius:20px;font-size:12px;color:#777;display:flex;align-items:center;padding-left:12px}
.signup .btn{top:64px;left:779px;width:148px;height:40px;font-size:11px}
.welcome-kicker{left:93px;top:828px;font-size:16px;color:var(--ink)}
.welcome-title{left:93px;top:850px;font-size:44px}
.welcome-text{left:93px;top:926px;width:495px;font-size:14.5px;line-height:21px}
/* featured */
.feature-box{left:745px;top:1336px;width:360px;height:339px;background:var(--red);color:var(--white)}
.feature-box .kicker{position:absolute;left:27px;top:30px;font-size:16px}
.feature-box h2{position:absolute;left:27px;top:50px;font-family:'Rubik',sans-serif;font-weight:800;font-size:46px}
.feature-box .rule{left:27px;top:107px;background:var(--white)}
.feature-box p{position:absolute;left:27px;top:126px;width:310px;font-size:14.5px;line-height:21px}
.section-title{left:0;width:1200px;text-align:center;font-size:46px}
/* events */
.event-card{position:absolute;top:2108px;width:464px;height:150px;background:var(--white);box-shadow:0 4px 14px rgba(0,0,0,.12)}
.pill{position:absolute;left:20px;top:16px;background:var(--red);color:var(--white);font-family:'Rubik',sans-serif;font-weight:700;font-size:10px;padding:3px 10px;border-radius:10px}
.event-card h3{position:absolute;left:21px;top:40px;width:430px;font-family:'Rubik',sans-serif;font-weight:400;font-size:20px;line-height:24px;color:var(--ink)}
.read-more{position:absolute;left:21px;top:116px;font-family:'Rubik',sans-serif;font-weight:700;font-size:10px;color:var(--ink);text-decoration:underline;letter-spacing:.5px}
/* news */
.news-band{left:0;top:2313px;width:1200px;height:610px;background:var(--grey)}
.news-intro{left:495px;top:2365px;width:600px;font-size:14.5px;line-height:24px;color:var(--ink)}
.news-card{position:absolute;top:2437px;width:321px;height:388px;background:var(--white);box-shadow:0 4px 14px rgba(0,0,0,.12)}
.news-card .photo{left:0;top:0;width:321px;height:205px}
.news-card h3{position:absolute;left:19px;top:228px;width:285px;font-family:'Rubik',sans-serif;font-weight:400;font-size:18px;line-height:24px;color:var(--ink)}
.news-card .rule{left:19px;top:332px;width:70px;height:1.5px}
.news-card time{position:absolute;left:23px;top:348px;font-size:11px;color:var(--ink)}
.pager{left:225px;top:2862px;font-family:'Rubik',sans-serif;font-size:12px;color:var(--ink)}
.pager .on{color:var(--red)}
/* support */
.support{left:0;top:2923px;width:1200px;height:205px;background:linear-gradient(90deg,#1b1d21,#2b2d33 50%,#1b1d21)}
.support-title{left:261px;top:3000px;font-family:'Rubik',sans-serif;font-size:44px;color:var(--white);font-weight:400;letter-spacing:-.5px}
.support-title b{font-weight:800}
/* stories */
.story{position:absolute}
.story .name{position:absolute;left:19px;bottom:86px;font-family:'Rubik',sans-serif;font-size:17px;color:var(--white)}
.story .sub{position:absolute;left:19px;bottom:66px;font-size:14px;font-style:italic;color:rgba(255,255,255,.75)}
.story .social{position:absolute;left:19px;bottom:32px;display:flex;gap:9px}
.social span{width:22px;height:22px;border:1px solid var(--white);border-radius:50%;display:block}
/* footer */
.site-footer{left:0;top:3624px;width:1200px;height:376px;background:var(--dark);color:#c9c9c9}
.foot-h{position:absolute;top:70px;font-family:'Rubik',sans-serif;font-weight:700;font-size:15px;color:var(--white)}
.foot-p{position:absolute;left:93px;top:108px;width:295px;font-size:13px;line-height:19.5px}
.foot-links{position:absolute;left:521px;top:108px;list-style:none;font-size:13px;line-height:19px}
.foot-links li{margin-bottom:11px;width:140px}
.badge{position:absolute;background:#fff}
.foot-rule{position:absolute;left:93px;top:318px;width:1014px;height:1px;background:#3d4046}
.copy{position:absolute;left:93px;top:341px;font-size:12px}
.copy span{color:var(--red)}
.top-btn{position:absolute;left:1054px;top:320px;width:53px;height:56px;background:var(--red)}
</style>
</head>
<body>

<div class="abs alert-bar">Aenean venenatis ipsum eu lacus ornare sodales. Nulla facilisi. Sed consectetur tincidunt ligula praesent maximus ex sit amet dolor consequat</div>

<header class="abs site-header">
  <div class="abs brand"><span class="brand-dot"></span><span>VALOR<br>FOUNDATION</span></div>
  <div class="btn donate-top">Donate</div>
  <nav class="abs main-nav"><span>About</span><span>Featured Action</span><span>Event</span><span>Latest News</span><span>Worker and member stories</span></nav>
</header>

<section class="abs hero" role="img" aria-label="Close-up of many hands stacked together in unity">
  <h1 class="abs hero-title">Join the<br>Peasant Movement</h1>
  <div class="abs slides"><div class="on">01 —</div><div>02</div><div>03</div></div>
</section>

<div class="abs intro-band"></div>

<form class="abs signup">
  <h2>SIGNUP</h2>
  <div class="field" style="left:30px">Name</div>
  <div class="field" style="left:280px">Email</div>
  <div class="field" style="left:529px">Zip Code</div>
  <div class="btn btn-red">Signup now</div>
</form>

<div class="abs welcome-kicker">WELCOME TO</div>
<h2 class="abs heading welcome-title">VALOR ANDES</h2>
<div class="rule" style="left:95px;top:905px"></div>
<p class="abs welcome-text">The Peasant Union Foundation is a dynamic non-profit organization established in 2006. The fundamental purpose of the Valor Foundation is to empower communities to ensure human dignity. We serve more than 90,000 immigrants annually through a holistic approach; we provide critical services and engage our constituents in systemic change to break the cycle of poverty.</p>
<div class="btn btn-red" style="left:95px;top:1080px;width:160px;height:44px">Read more</div>
<div class="photo" style="left:774px;top:796px;width:333px;height:244px;background:linear-gradient(160deg,#c8bfae,#8f8a80 60%,#6d6e6a)" role="img" aria-label="Volunteers in masks carrying food boxes in a parking lot"></div>
<div class="photo" style="left:652px;top:953px;width:244px;height:178px;background:linear-gradient(170deg,#a9b3b4,#6d5a55 60%,#4a3d3c)" role="img" aria-label="Line of cars at a drive-through food distribution"></div>

<div class="photo" style="left:95px;top:1276px;width:810px;height:442px;background:linear-gradient(135deg,#8a6a4c,#a08466 40%,#6d6a45 70%,#4e4a32)" role="img" aria-label="Volunteer giving thumbs up beside collected trash bags in a park"></div>
<div class="abs feature-box">
  <div class="kicker">FEATURED</div>
  <h2>ACTION</h2>
  <div class="rule"></div>
  <p>Lorem ipsum dolor sit amt, conetur adiiscing elit. Mauris congue enim est, vitae feugiat mauris porttitor id. Vestibulum aliquam, eros nec volutpat rhoncus, nisi ipsum bibendum dolor, non porta ipsum</p>
  <div class="btn btn-line" style="left:27px;top:261px;width:160px;height:44px">Read more</div>
</div>

<h2 class="abs heading section-title" style="top:1756px">LATEST EVENT</h2>
<div class="rule" style="left:575px;top:1815px"></div>
<div class="photo" style="left:95px;top:1839px;width:496px;height:303px;background:linear-gradient(170deg,#b8c6d4,#7f8f7a 55%,#9a9a98)" role="img" aria-label="Outdoor event with canopy tents and families waiting in line"></div>
<div class="photo" style="left:610px;top:1839px;width:497px;height:303px;background:linear-gradient(170deg,#c5d2dc,#c9b9a5 50%,#8a8a86)" role="img" aria-label="Youth center entrance with a distribution tent and volunteers"></div>
<article class="event-card" style="left:112px"><span class="pill">Oct 17, 2020</span><h3>Pellentesque ultrices quis orci quis tristique aenean venenatis</h3><span class="read-more">READ MORE</span></article>
<article class="event-card" style="left:627px"><span class="pill">Oct 22, 2020</span><h3>Pellentesque ultrices quis orci quis tristique aenean venenatis</h3><span class="read-more">READ MORE</span></article>

<section class="abs news-band"></section>
<h2 class="abs heading" style="left:93px;top:2354px;font-size:46px">LATEST NEWS</h2>
<div class="rule" style="left:95px;top:2413px"></div>
<p class="abs news-intro">The Peasant Union Foundation is a dynamic non-profit organization established in 2006. The fundamental purpose of the Valor Foundation is to empower</p>
<article class="news-card" style="left:95px"><div class="photo" style="background:linear-gradient(170deg,#9aa2a8,#b89a6a 55%,#7d7a73)" role="img" aria-label="Volunteer in a safety vest at a roadside food distribution"></div><h3>Common Table Kitchen &amp; the Peasant Movement distribute meals for families of peasant workers</h3><div class="rule"></div><time>April 22, 2020 6:00 PM</time></article>
<article class="news-card" style="left:439px"><div class="photo" style="background:linear-gradient(170deg,#8d8b86,#b6b3ad 55%,#8a8680)" role="img" aria-label="Masked volunteer handing a box to a driver through a car window"></div><h3>Federal Proposed H-2A Guest Worker Program Rules Would Harm, Not Help, Farmworkers</h3><div class="rule"></div><time>July 26, 2019</time></article>
<article class="news-card" style="left:784px"><div class="photo" style="background:linear-gradient(170deg,#c9b08a,#a77f55 55%,#8c7766)" role="img" aria-label="Volunteer in a red vest among stacked supply boxes"></div><h3>Valor Foundation on Introducing the Harvest Futures Act</h3><div class="rule"></div><time>Juno 04, 2019</time></article>
<div class="abs pager"><span class="on">01</span> / 03</div>
<div class="abs" style="left:269px;top:2869px;width:619px;height:1px;background:#b9b9b9"></div>
<div class="abs" style="left:269px;top:2868px;width:45px;height:2px;background:var(--red)"></div>
<svg class="abs" style="left:905px;top:2862px" width="34" height="14" viewBox="0 0 34 14" fill="none" stroke="#555" stroke-width="1.3"><path d="M8 2 3 7l5 5M26 2l5 5-5 5"/></svg>

<section class="abs support" role="img" aria-label="Dark faded photo of foundation supporters with a banner">
</section>
<h2 class="abs support-title">SUPPORT OUR <b>WORK</b></h2>
<div class="btn btn-red" style="left:740px;top:3000px;width:197px;height:50px;font-size:13px;letter-spacing:5px">Donate now</div>

<h2 class="abs heading section-title" style="top:3175px">WORKER AND MEMBER STORIES</h2>
<div class="rule" style="left:575px;top:3235px"></div>
<div class="story" style="left:95px;top:3279px;width:243px;height:291px;background:linear-gradient(180deg,#e3e3e3,#b7a593 60%,#6f6a66)" role="img" aria-label="Portrait of a smiling member in a yellow shirt"><div class="name">Cras euismod purus</div><div class="sub">sed leo consequat</div><div class="social"><span></span><span></span><span></span></div></div>
<div class="story" style="left:607px;top:3279px;width:245px;height:291px;background:linear-gradient(180deg,#e8e8e8,#c79a86 60%,#8e6d62)" role="img" aria-label="Portrait of a member in a coral shirt"><div class="name">Cras euismod purus</div><div class="sub">sed leo consequat</div><div class="social"><span></span><span></span><span></span></div></div>
<div class="story" style="left:852px;top:3279px;width:253px;height:291px;background:linear-gradient(180deg,#e6e6e6,#8a7f7e 55%,#39477a)" role="img" aria-label="Portrait of a smiling member in a blue shirt"><div class="name">Cras euismod purus</div><div class="sub">sed leo consequat</div><div class="social"><span></span><span></span><span></span></div></div>
<div class="story" style="left:338px;top:3261px;width:269px;height:324px;background:linear-gradient(180deg,#ececec,#c9b09a 55%,#2c2c2c);box-shadow:0 6px 18px rgba(0,0,0,.25)" role="img" aria-label="Portrait of a member in a black t-shirt"><div class="name">Cras euismod purus</div><div class="sub">sed leo consequat</div><div class="social"><span></span><span></span><span></span></div>
  <svg style="position:absolute;right:0;bottom:0" width="51" height="49" viewBox="0 0 51 49"><rect width="51" height="49" fill="#fff"/><path d="M16 24.5h19M29 18l7 6.5-7 6.5" fill="none" stroke="#dc0000" stroke-width="2"/></svg>
</div>

<footer class="abs site-footer">
  <h4 class="foot-h" style="left:93px">Our Mission</h4>
  <p class="foot-p">The Peasant Union Foundation is a dynamic non-profit organization established in 2006. The fundamental purpose of the Valor Foundation is to empower communities to ensure human dignity. We serve more than 90,000 immigrants annually through a holistic approach; we provide critical services</p>
  <h4 class="foot-h" style="left:521px">Quick Links</h4>
  <ul class="foot-links"><li>About</li><li>Featured Action</li><li>Event</li><li>Latest News</li><li>Worker and member stories</li><li>Donate</li></ul>
  <div class="badge" style="left:752px;top:122px;width:76px;height:28px;border-radius:3px"></div>
  <div class="badge" style="left:902px;top:115px;width:44px;height:44px;border-radius:50%"></div>
  <div class="badge" style="left:1018px;top:122px;width:88px;height:32px;border-radius:3px"></div>
  <div class="badge" style="left:763px;top:206px;width:56px;height:56px;border-radius:50%"></div>
  <div class="badge" style="left:862px;top:208px;width:46px;height:50px;border-radius:4px"></div>
  <div class="badge" style="left:945px;top:214px;width:46px;height:38px;border-radius:3px"></div>
  <div class="badge" style="left:1050px;top:206px;width:56px;height:56px;border-radius:50%"></div>
  <div class="foot-rule"></div>
  <p class="copy">© 2020 <span>valor andes</span>. All Right Reserved.</p>
  <div class="top-btn"><svg width="53" height="56" viewBox="0 0 53 56"><path d="M15 34l11.5-12L38 34" fill="none" stroke="#fff" stroke-width="2"/></svg></div>
</footer>

</body>
</html>
```